Bluefern painting and decorating *

Need a flyer design to advertise my services
So the information I need included is the services we offer at bluefern painting and decorating which include
Interior painting
Exterior painting
Wallpaper hanging
Paint and cellulose spraying
Dust free sanding
Pressure washing
Stone cleaning
Also would need to have my company contact details in
Www.bluefernpaintingdecorating.co.uk
Email is info@bluefernpaintingdecorating.com
Bluefern Painting & Decorating Services has a proven track record of innovative designs, effective problem solving and attention to detail and our goal is to meet and exceed the expectations of every customer. We take on all types of jobs from small domestic work to larger commercial projects, all carried out to the highest standards, and at very competitive prices.

```html
<!DOCTYPE html>
<html lang="en">
<head>
<meta charset="utf-8">
<title>Bluefern Painting &amp; Decorating – Flyer</title>
<link rel="stylesheet" href="https://fonts.googleapis.com/css2?family=Open+Sans:wght@400;600;700;800&display=swap">
<style>
  :root{
    --navy:#0f4a86;
    --blue:#2a86cc;
    --teal:#2a9ad0;
    --band:#1c84bf;
    --footer:#3f3f3f;
    --page:#e9ecef;
    --white:#ffffff;
    --list:#1f5f9c;
    --body-text:#3d4f63;
  }
  *{box-sizing:border-box;margin:0;padding:0}
  html,body{width:1040px;height:1200px;overflow:hidden;background:var(--page);font-family:"Open Sans",Arial,sans-serif}
  .flyer{position:absolute;left:56px;top:6px;width:928px;height:1188px;background:var(--white);overflow:hidden;box-shadow:0 6px 18px rgba(0,0,0,.18)}
  .hero-photo{position:absolute;left:0;top:0;width:928px;height:544px;
    background:linear-gradient(180deg,#eef0ef 0%,#d8d3c8 35%,#9d968b 60%,#c9b79b 100%)}
  .header-shape{position:absolute;left:0;top:0;width:928px;height:180px}
  .brand{position:absolute;left:38px;top:52px;width:330px;color:var(--navy);font-weight:800;font-size:27px;line-height:1.15;letter-spacing:.5px;text-transform:uppercase}
  .brand-dot{display:inline-block;width:12px;height:12px;border-radius:50%;background:var(--navy);margin-right:8px;vertical-align:2px}
  .headline{position:absolute;left:0;width:928px;text-align:center;font-weight:700;text-transform:uppercase;paint-order:stroke fill}
  .headline-main{top:360px;font-size:52px;color:#0e3f75;-webkit-text-stroke:3px #fff;letter-spacing:.5px}
  .headline-sub{top:420px;font-size:40px;color:#2a9ad0;-webkit-text-stroke:2.5px #fff}
  .sector{position:absolute;top:497px;width:262px;height:180px;background:var(--blue)}
  .sector-title{position:absolute;top:30px;width:100%;text-align:center;color:#fff;font-weight:700;font-size:18px}
  .sector-ring{position:absolute;top:550px;width:240px;height:240px;border-radius:50%;border:1.5px solid var(--blue)}
  .sector-photo{position:absolute;top:4px;left:4px;width:229px;height:229px;border-radius:50%}
  .photo-commercial{background:linear-gradient(180deg,#eef0f0,#9b9a97 60%,#bca98c)}
  .photo-yellow{background:radial-gradient(circle at 50% 40%,#ffd25a,#f2b63c 70%,#d9a35b)}
  .photo-lounge{background:linear-gradient(180deg,#d9ccb3,#8b7a6a 55%,#e6e1da)}
  .services-title{position:absolute;top:800px;left:0;width:928px;text-align:center}
  .services-title span{display:inline-block;color:var(--teal);font-weight:700;font-size:30px;text-transform:uppercase;border-bottom:1.5px solid var(--teal);padding-bottom:2px;line-height:1.2}
  .company-intro{position:absolute;top:852px;left:86px;width:756px;text-align:center;color:var(--body-text);font-size:13px;line-height:18px}
  .service-list{position:absolute;top:918px;list-style:none}
  .service-list li{position:relative;height:27px;line-height:27px;font-size:17px;letter-spacing:3.6px;color:var(--list);text-transform:uppercase;padding-left:38px}
  .service-list li::before{content:"";position:absolute;left:0;top:12px;width:9px;height:9px;border-radius:50%;background:#1d5ea8}
  .list-left{left:86px}
  .list-right{left:472px}
  .phone-band{position:absolute;left:0;top:1047px;width:928px;height:83px;background:var(--band);color:#fff;text-align:center;font-weight:700;font-size:48px;line-height:83px;letter-spacing:1px}
  .contact-footer{position:absolute;left:0;top:1130px;width:928px;height:58px;background:var(--footer);color:#fff;text-align:center;font-size:14px;line-height:58px;letter-spacing:.4px}
  .contact-footer span+span{margin-left:14px}
  .footer-web{text-transform:uppercase}
</style>
</head>
<body>
<main class="flyer">
  <div class="hero-photo" role="img" aria-label="Photo of a bright modern lounge with grey sofas and armchairs on a light wood floor"></div>
  <svg class="header-shape" viewBox="0 0 928 180" aria-hidden="true">
    <defs>
      <linearGradient id="swoosh" x1="0" x2="1" y1="0" y2="0">
        <stop offset="0" stop-color="#1c5fb0"/>
        <stop offset="1" stop-color="#2a8ad4"/>
      </linearGradient>
    </defs>
    <path d="M0 0 H928 V70 C850 20 720 8 600 30 C470 60 380 120 220 145 C140 156 60 160 0 162 Z" fill="#fff"/>
    <path d="M0 140 C180 150 330 130 440 80 C500 52 540 24 575 0 L560 0 C520 20 470 48 420 72 C300 120 160 136 0 128 Z" fill="url(#swoosh)"/>
  </svg>
  <div class="brand"><span class="brand-dot"></span>Bluefern painting and decorating</div>

  <h1 class="headline headline-main">Established decorators</h1>
  <h2 class="headline headline-sub">In South London</h2>

  <section class="sector" style="left:55px"><div class="sector-title">COMMERCIAL</div></section>
  <section class="sector" style="left:341px"><div class="sector-title">DOMESTIC</div></section>
  <section class="sector" style="left:628px"><div class="sector-title">DOMESTIC</div></section>

  <div class="sector-ring" style="left:66px"><div class="sector-photo photo-commercial" role="img" aria-label="Photo of a commercial lounge with grey seating"></div></div>
  <div class="sector-ring" style="left:352px"><div class="sector-photo photo-yellow" role="img" aria-label="Photo of a yellow painted wall behind a pale yellow sofa with a plant"></div></div>
  <div class="sector-ring" style="left:639px"><div class="sector-photo photo-lounge" role="img" aria-label="Photo of a decorated living room with curtains, wallpaper and white sofas"></div></div>

  <div class="services-title"><span>Our range of services include:</span></div>
  <p class="company-intro">Bluefern Painting &amp; Decorating Services has a proven track record of innovative designs, effective problem solving and attention to detail, and our goal is to meet and exceed the expectations of every customer. We take on all types of jobs from small domestic work to larger commercial projects, all carried out to the highest standards, and at very competitive prices.</p>
  <ul class="service-list list-left">
    <li>Interior painting</li>
    <li>Exterior painting</li>
    <li>Wallpaper hanging</li>
    <li>Pressure washing</li>
  </ul>
  <ul class="service-list list-right">
    <li>Paint and cellulose spraying</li>
    <li>Dust free sanding</li>
    <li>Stone cleaning</li>
  </ul>

  <div class="phone-band">07700 900 318</div>
  <footer class="contact-footer">
    <span class="footer-web">www.bluefernpaintingdecorating.co.uk</span>
    <span>EMAIL: info@bluefernpaintingdecorating.com</span>
  </footer>
</main>
</body>
</html>
```